my catalog design project for KRV tradeshow

We need a catalog design for our ranch equipment manufacturing company. The final design should communicate low cost alternative without compromising quality.
We need all the main product lines show cased in catalog including gates, panels, feeders, cattle squeezes, horse stalls, dog kennels, tractor attachments
The layout, design and colors can reflect the design of the website:

We just need a basic product catalog that uses a similar layout, design, and colors as our website: quillbarnfabricating.com

Catalog should be approximately 6-10 pages long 8.5"x11" first page cover, next inside page company info, then product pages with item picture and description as in the website. For sample submissions, i'd like to see cover page, inside page and a product page.

FOR THE INITIAL ENTRIES, I'm expecting to see
- the cover page,
- inside company info page
- and one product page.

Target Market(s)

Chain Store buyers

Industry/Entity Type

Agriculture

Requirements
Must have
• All the product info details of main products

```html
<!DOCTYPE html>
<html lang="en">
<head>
<meta charset="utf-8">
<title>Frame Gates – Quill Barn Fabricating</title>
<link href="https://fonts.googleapis.com/css2?family=Montserrat:wght@600;700;800&family=Poppins:wght@400;500&display=swap" rel="stylesheet">
<style>
  :root {
    --brand-red: #7b1416;
    --band-gray: #e3e3e5;
    --row-gray: #e2e2e2;
    --ink: #1b1b1b;
    --paper: #ffffff;
    --photo-light: #f3f2f2;
    --photo-mid: #e6e3e3;
  }
  html, body {
    margin: 0;
    padding: 0;
    overflow: hidden;
    background: var(--paper);
  }
  .page {
    position: relative;
    width: 928px;
    height: 1200px;
    overflow: hidden;
    background: var(--paper);
    font-family: "Poppins", Arial, sans-serif;
    color: var(--ink);
  }
  .brand {
    position: absolute;
    left: 598px;
    top: 70px;
    display: flex;
    align-items: center;
    gap: 12px;
  }
  .brand-dot {
    width: 34px;
    height: 34px;
    border-radius: 50%;
    background: var(--brand-red);
  }
  .brand-name {
    font-family: "Montserrat", Arial, sans-serif;
    font-weight: 800;
    font-size: 19px;
    line-height: 1.05;
    color: var(--ink);
    letter-spacing: 0.5px;
  }
  .top-band {
    position: absolute;
    left: 179px;
    top: 164px;
    width: 749px;
    height: 18px;
    background: var(--band-gray);
  }
  .title-band {
    position: absolute;
    left: 179px;
    top: 186px;
    width: 749px;
    height: 81px;
    background: var(--brand-red);
    display: flex;
    align-items: center;
  }
  .title-band h1 {
    margin: 0 0 0 29px;
    font-family: "Montserrat", Arial, sans-serif;
    font-weight: 700;
    font-size: 27px;
    letter-spacing: 1.5px;
    color: var(--paper);
    display: flex;
    align-items: center;
    gap: 12px;
  }
  .title-band h1 svg { display: block; }
  .product-photo {
    position: absolute;
    left: 144px;
    top: 274px;
    width: 530px;
    height: 348px;
    background: linear-gradient(135deg, var(--photo-light), var(--photo-mid));
  }
  .section-heading {
    position: absolute;
    left: 178px;
    top: 654px;
    margin: 0;
    font-family: "Poppins", Arial, sans-serif;
    font-weight: 500;
    font-size: 20px;
    letter-spacing: -0.2px;
    color: var(--brand-red);
  }
  .spec-table {
    position: absolute;
    left: 179px;
    top: 740px;
    width: 617px;
    border-collapse: separate;
    border-spacing: 0;
    font-size: 13px;
  }
  .spec-table th {
    font-family: "Montserrat", Arial, sans-serif;
    font-weight: 700;
    font-size: 16px;
    line-height: 20px;
    text-align: left;
    padding: 0 4px 12px 3px;
    border-bottom: 5px solid var(--brand-red);
  }
  .spec-table th.weight { text-align: right; padding-right: 0; }
  .spec-table td {
    background: var(--row-gray);
    height: 28px;
    padding: 0 0 0 12px;
    border-bottom: 2px solid var(--paper);
  }
  .spec-table td.weight {
    text-align: center;
    padding: 0;
    border-left: 2px solid var(--paper);
    width: 119px;
  }
  .spec-table tr.spec-row td { height: 50px; vertical-align: top; padding-top: 10px; }
  .spec-table tr.spec-row td.weight { font-size: 14px; vertical-align: middle; padding-top: 4px; }
</style>
</head>
<body>
<div class="page">
  <div class="brand">
    <div class="brand-dot"></div>
    <div class="brand-name">QUILL BARN<br>FABRICATING</div>
  </div>

  <div class="top-band"></div>
  <div class="title-band">
    <h1>
      <svg width="11" height="13" viewBox="0 0 11 13" aria-hidden="true"><polygon points="0,0 11,6.5 0,13" fill="#ffffff"/></svg>
      FRAME GATES
    </h1>
  </div>

  <div class="product-photo" role="img" aria-label="Photo of two red steel frame gates with six rails and plunger latches"></div>

  <h2 class="section-heading">Frame Gates</h2>

  <table class="spec-table">
    <thead>
      <tr><th>DESCRIPTION</th><th class="weight">WEIGHT Es.</th></tr>
    </thead>
    <tbody>
      <tr class="spec-row"><td>2-5/16" x 15ga. Sq. Corner, Al saddle Joint, w/ Plunger Latch</td><td class="weight">In Pounds</td></tr>
      <tr><td>6' Frame Gate, Six Rail - 6'10" Tall w/ Plunger Latch</td><td class="weight">125</td></tr>
      <tr><td>10' Frame Gate, Six Rail - 8'4" Tall w/ Plunger Latch</td><td class="weight">238</td></tr>
      <tr><td>12' Frame Gate, Six Rail - 8'4" Tall w/ Plunger Latch</td><td class="weight">268</td></tr>
      <tr><td>12' Frame Gate, Six Rail - 10' Tall w/ Plunger Latch</td><td class="weight">280</td></tr>
    </tbody>
  </table>
</div>
</body>
</html>
```